Need to make a KTR water label for my water bottle and packaging. Attached is our Trademarked LOGO for KTR we have a natural spring water that flows through our land that is naturally filtered through pure limestone. want to make a badass label that has our logo in it with our colors

Target Market(s)

Commercial Bottle water

Colors
3176b5

```html
<!DOCTYPE html>
<html lang="en">
<head>
<meta charset="utf-8">
<title>KTR Natural Spring Water – Label</title>
<link rel="stylesheet" href="https://fonts.googleapis.com/css2?family=Roboto+Condensed:wght@400;700&display=swap">
<style>
  :root {
    --brand-blue: #3176b5;
    --label-blue: #2f8ad0;
    --light-blue: #8fd0f5;
    --deep-blue: #1d5f9c;
    --ink: #16304d;
    --stage: #eceef1;
    --paper: #ffffff;
  }
  * { box-sizing: border-box; margin: 0; padding: 0; }
  html, body { width: 1200px; height: 1200px; overflow: hidden; }
  body {
    background: radial-gradient(circle at 50% 45%, #ffffff 0%, var(--stage) 75%);
    font-family: "Roboto Condensed", "Arial Narrow", sans-serif;
    color: var(--ink);
  }
  .label {
    position: absolute; left: 40px; top: 300px;
    width: 1120px; height: 600px;
    background: var(--paper);
    border-radius: 6px;
    box-shadow: 0 20px 50px rgba(20, 50, 90, 0.15);
    overflow: hidden;
  }
  .ridge-art {
    position: absolute; left: 0; top: 30px; width: 100%; height: 90px;
    background: linear-gradient(to bottom, var(--paper) 0%, var(--light-blue) 55%, var(--label-blue) 100%);
  }
  .label-band {
    position: absolute; left: 0; top: 120px; width: 100%; height: 360px;
    background: var(--label-blue);
  }
  .bubble-art {
    position: absolute; left: 0; top: 480px; width: 100%; height: 120px;
    background: linear-gradient(to bottom, var(--label-blue) 0%, var(--light-blue) 45%, var(--paper) 100%);
  }
  .panel { position: absolute; top: 0; height: 100%; }
  .panel-info { left: 0; width: 373px; }
  .panel-front { left: 373px; width: 374px; }
  .panel-story { left: 747px; width: 373px; }

  /* front panel */
  .brand {
    position: absolute; left: 0; right: 0; top: 118px;
    display: flex; align-items: center; justify-content: center; gap: 12px;
  }
  .brand-dot { width: 30px; height: 30px; border-radius: 50%; background: var(--paper); }
  .brand-name { font-size: 64px; font-weight: 700; color: var(--paper); letter-spacing: 2px; line-height: 1; }
  .product-title {
    position: absolute; left: 0; right: 0; top: 205px;
    text-align: center; color: var(--paper);
    font-size: 60px; font-weight: 700; line-height: 1.02;
  }
  .product-sub {
    position: absolute; left: 0; right: 0; top: 338px;
    text-align: center; font-size: 25px; color: var(--ink);
  }
  .origin-seal {
    position: absolute; left: 30px; top: 385px;
    width: 84px; height: 84px; border-radius: 50%;
    background: var(--brand-blue); border: 6px solid var(--paper);
  }
  .volume {
    position: absolute; left: 283px; top: 392px;
    width: 78px; height: 78px; border-radius: 50%;
    background: var(--deep-blue); border: 3px solid var(--paper);
    display: flex; align-items: center; justify-content: center;
    font-size: 22px; font-weight: 700; color: var(--ink);
  }

  /* info panel */
  .info-head { position: absolute; left: 34px; top: 150px; font-size: 17px; font-weight: 700; color: var(--ink); }
  .info-text { position: absolute; left: 34px; top: 172px; width: 300px; font-size: 12px; line-height: 1.25; color: var(--ink); }
  .minerals {
    position: absolute; left: 34px; top: 212px; width: 230px;
    background: var(--paper); font-size: 11.5px;
    border-collapse: collapse;
  }
  .minerals caption { text-align: left; font-size: 13px; padding: 6px 10px 4px; background: var(--paper); }
  .minerals td { border-bottom: 1px solid #333; padding: 3px 10px; }
  .minerals td.value { text-align: right; }

  /* story panel */
  .story-head { position: absolute; left: 30px; right: 30px; top: 160px; text-align: center; font-size: 18px; font-weight: 700; color: var(--ink); }
  .story-text { position: absolute; left: 36px; right: 36px; top: 190px; text-align: center; font-size: 14px; line-height: 1.35; color: var(--ink); }
</style>
</head>
<body>
<main class="label">
  <div class="ridge-art" role="img" aria-label="Mountain ridge silhouette along the top of the label"></div>
  <div class="label-band"></div>
  <div class="bubble-art" role="img" aria-label="Rising water bubbles along the bottom of the label"></div>

  <section class="panel panel-info">
    <h3 class="info-head">Kettle Ridge Limestone</h3>
    <p class="info-text">Water from Kettle Ridge is filtered through stone, which ensures a pureness you have never tasted before.</p>
    <table class="minerals">
      <caption>Mineral composition in mg/liter.</caption>
      <tr><td>Calcium</td><td class="value">23</td></tr>
      <tr><td>Magnesium</td><td class="value">13</td></tr>
      <tr><td>Potassium</td><td class="value">3</td></tr>
      <tr><td>Bicarbonate</td><td class="value">126</td></tr>
      <tr><td>Fluoride</td><td class="value">0.3</td></tr>
      <tr><td>Silica</td><td class="value">8.7</td></tr>
      <tr><td>Nitrate</td><td class="value">0.36</td></tr>
      <tr><td>Sulfate</td><td class="value">13</td></tr>
      <tr><td>Total dissolved solids</td><td class="value">159</td></tr>
      <tr><td>Chloride</td><td class="value">14</td></tr>
    </table>
  </section>

  <section class="panel panel-front">
    <div class="brand"><span class="brand-dot"></span><span class="brand-name">KTR</span></div>
    <h1 class="product-title">Natural<br>Spring Water</h1>
    <p class="product-sub">Filtered Through Natural Limestone</p>
    <div class="origin-seal"></div>
    <div class="volume">500ml</div>
  </section>

  <section class="panel panel-story">
    <h2 class="story-head">Kettle Ridge Limestone</h2>
    <p class="story-text">water rises slowly through layers of ancient limestone deep beneath our land. Every drop is naturally filtered over many years, gathering a balanced blend of minerals along the way. We bottle it right at the source, untouched and unhurried, so it reaches you exactly as nature made it: clean, crisp and refreshingly smooth.</p>
  </section>
</main>
</body>
</html>
```